Blockchain Analytics Firm Needs Logo And Website Design

We need a logo and a very basic website for a company based in Linköping, Sweden called 'Vextrel'. We build custom machine learning and AI solutions for companies based on blockchain. We are not picky about the colors, but the design should communicate modernity and stability.
We like the following websites:
https://www.tallowmeadow.co.uk/
https://www.corvanholdings.com/
Target Market(s)
Our customers are startups that have their own product based on blockchain or other distributed ledger technology.
Industry/Entity Type
It Company
Contact Information for Business Card
Name, title and email address
Logo Text
Our company name and "Blockchain Analytics"
Colors
Designer to choose colors to be used in the design.
Requirements
Must have
- The website and logo need to be modern and clean. In the beginning, we will not be filling out all sections of the website (team, clients, etc.) but we will need to have these set up so we can eventually use them.
Nice to have
- We like angular graphics and some animations on the webpage would be nice.

```html
<!DOCTYPE html>
<html lang="en">
<head>
<meta charset="utf-8">
<title>Vextrel — Blockchain Analytics</title>
<link rel="stylesheet" href="https://fonts.googleapis.com/css2?family=Questrial&family=Open+Sans:wght@400;600&display=swap">
<style>
:root{
  --header:#262626;
  --footer:#222222;
  --red:#e8453c;
  --heading-red:#dc4b44;
  --nav-blue:#4da3ff;
  --purple:#6b4de0;
  --text:#333333;
  --muted:#8a8a8a;
  --band:#efefef;
  --white:#ffffff;
  --diamond:#2b2b2b;
  --field:#2c2c2c;
  --field-line:#444444;
}
*{margin:0;padding:0;box-sizing:border-box}
html,body{width:1200px;height:2821px;overflow:hidden}
body{position:relative;background:var(--white);font-family:"Open Sans",Arial,sans-serif;color:var(--text)}
.abs{position:absolute}
.site-header{left:0;top:0;width:1200px;height:130px;background:var(--header)}
.brand{left:132px;top:28px;display:flex;align-items:center;gap:14px}
.brand-mark{width:48px;height:48px;background:var(--red)}
.brand-name{font-family:"Questrial",sans-serif;font-size:32px;line-height:34px;color:var(--red);letter-spacing:1px}
.brand-tag{font-family:"Questrial",sans-serif;font-size:19px;line-height:22px;color:var(--nav-blue)}
.member-login{left:946px;top:24px;width:120px;height:33px;background:var(--red);color:var(--white);font-size:13px;line-height:33px;text-align:center;border-radius:2px}
.main-nav{top:82px;left:0;width:1200px;height:20px}
.main-nav span{position:absolute;transform:translateX(-50%);font-size:14px;color:var(--white);white-space:nowrap}
.main-nav .active{color:var(--nav-blue)}
.hero{left:0;top:130px;width:1200px;height:483px;background:linear-gradient(120deg,#4b3cf0 0%,#5a5cf6 45%,#7a78f5 70%,#5e46ea 100%)}
.hero-title{left:0;top:290px;width:1200px;text-align:center;font-family:"Questrial",sans-serif;font-size:37px;line-height:47px;color:var(--white)}
.hero-btn{left:538px;top:397px;width:122px;height:45px;background:var(--white);color:var(--red);font-size:15px;line-height:45px;text-align:center}
.welcome-title{left:0;top:686px;width:1200px;text-align:center;font-family:"Questrial",sans-serif;font-size:38px;color:var(--heading-red)}
.welcome-text{left:132px;top:738px;width:936px;text-align:center;font-size:16.5px;line-height:29px;color:var(--text)}
.dashboard-shot{left:132px;top:890px;width:934px;height:549px;background:linear-gradient(90deg,#1f2a38 0 15%,#eef0f2 15% 100%)}
.video{left:0;top:1520px;width:1200px;height:402px;background:radial-gradient(ellipse at 55% 40%,#4a4a55 0%,#2a2a30 55%,#18181c 100%)}
.features .item{position:absolute;width:330px;text-align:center}
.feature-title{font-family:"Questrial",sans-serif;font-size:23px;color:var(--purple);margin-bottom:8px}
.feature-text{font-size:14px;line-height:19px;color:var(--text)}
.partners{left:0;top:2389px;width:1200px;height:118px;background:var(--band)}
.partner{position:absolute;top:47px;transform:translateX(-50%);font-family:"Open Sans",sans-serif;font-weight:600;font-size:19px;color:#1a1a1a;display:flex;align-items:center;gap:7px;white-space:nowrap}
.partner i{display:block;width:14px;height:14px;background:#1a1a1a}
.site-footer{left:0;top:2507px;width:1200px;height:314px;background:var(--footer);color:var(--muted);font-size:12px}
.footer-head{position:absolute;top:57px;font-family:"Questrial",sans-serif;font-size:15px;color:#cfcfcf;letter-spacing:.5px}
.footer-link{position:absolute;font-size:11.5px;color:var(--muted)}
.field{position:absolute;border:1px solid var(--field-line);background:var(--field);color:#777;font-size:11.5px;padding:7px 12px}
.send{position:absolute;left:1012px;top:130px;width:54px;height:31px;background:#4a4a4a;color:#ddd;font-size:11px;line-height:31px;text-align:center}
.rule{position:absolute;left:132px;top:211px;width:934px;height:1px;background:#3a3a3a}
.copyright{position:absolute;left:132px;top:250px;font-size:11.5px;color:#777}
.social{position:absolute;top:253px;width:14px;height:14px;border-radius:50%;background:#6d6d6d}
</style>
</head>
<body>
<header class="site-header abs">
  <div class="brand abs">
    <div class="brand-mark"></div>
    <div>
      <div class="brand-name">VEXTREL</div>
      <div class="brand-tag">Blockchain Analytics</div>
    </div>
  </div>
  <div class="member-login abs">Member Login</div>
  <nav class="main-nav abs">
    <span class="active" style="left:619px">Home</span>
    <span style="left:697px">Services</span>
    <span style="left:781px">Portfolio</span>
    <span style="left:858px">About</span>
    <span style="left:936px">Partners</span>
    <span style="left:1031px">Contact Us</span>
  </nav>
</header>

<section class="hero abs" role="img" aria-label="Blue-tinted photo of large interlocking chain links made of digital code"></section>
<svg class="abs" style="left:54px;top:362px" width="20" height="24" viewBox="0 0 20 24"><path d="M14 3 L5 12 L14 21" fill="none" stroke="#fff" stroke-width="3"/></svg>
<svg class="abs" style="left:1126px;top:362px" width="20" height="24" viewBox="0 0 20 24"><path d="M6 3 L15 12 L6 21" fill="none" stroke="#fff" stroke-width="3"/></svg>
<h1 class="hero-title abs">Pellentesque imperdiet dolor<br>et auctor est</h1>
<div class="hero-btn abs">Learn More</div>

<h2 class="welcome-title abs">Welcome to Vextrel</h2>
<p class="welcome-text abs">Vextrel is a data analytics startup that can quickly deploy custom machine learning and AI solutions for companies based on Distributed Ledger Technologies (DLT) such as Blockchains. &nbsp;A massive amount of data is generated from these Smart Contracts, particularly from Internet of Things (IoT) applications. &nbsp;We combine this information with traditional data pipelines and present a complete package to our customer.</p>

<div class="dashboard-shot abs" role="img" aria-label="Screenshot of the analytics dashboard with stat tiles, line and bar charts, a world map and an order table"></div>

<section class="video abs" role="img" aria-label="Video still of a speaker presenting on stage in front of the company name projected on a screen"></section>
<svg class="abs" style="left:570px;top:1691px" width="60" height="60" viewBox="0 0 60 60"><circle cx="30" cy="30" r="29" fill="#fff"/><path d="M24 18 L42 30 L24 42 Z" fill="#222"/></svg>

<section class="features">
  <svg class="abs" style="left:172px;top:2003px" width="212" height="212" viewBox="0 0 212 212"><path d="M106 0 L212 106 L106 212 L0 106 Z" fill="var(--diamond)"/>
    <g fill="none" stroke="#fff" stroke-width="2.5"><path d="M80 130 H132"/><rect x="84" y="112" width="8" height="18"/><rect x="97" y="102" width="8" height="28"/><rect x="110" y="94" width="8" height="36"/><rect x="123" y="84" width="8" height="46"/><path d="M84 100 L100 86 L110 92 L128 76"/><path d="M120 76 H128 V84"/></g></svg>
  <svg class="abs" style="left:493px;top:2003px" width="212" height="212" viewBox="0 0 212 212"><path d="M106 0 L212 106 L106 212 L0 106 Z" fill="var(--diamond)"/>
    <g fill="none" stroke="#fff" stroke-width="2.5"><rect x="80" y="80" width="16" height="14"/><rect x="116" y="80" width="16" height="14"/><rect x="98" y="99" width="16" height="14"/><rect x="80" y="118" width="16" height="14"/><rect x="116" y="118" width="16" height="14"/><path d="M96 87 H116 M88 94 V118 M124 94 V118 M96 125 H116 M106 113 V125"/></g></svg>
  <svg class="abs" style="left:814px;top:2003px" width="212" height="212" viewBox="0 0 212 212"><path d="M106 0 L212 106 L106 212 L0 106 Z" fill="var(--diamond)"/>
    <g fill="none" stroke="#fff" stroke-width="3"><circle cx="100" cy="100" r="18"/><path d="M113 113 L132 132"/></g></svg>
  <div class="item" style="left:113px;top:2226px"><div class="feature-title">MAECENAS VEL</div><p class="feature-text">As more and more people own cryptocurrencies,<br>interest in using them as a means of payment<br>increases.</p></div>
  <div class="item" style="left:435px;top:2226px"><div class="feature-title">AENEAN FACILISIS</div><p class="feature-text">As more and more people own cryptocurrencies,<br>interest in using them as a means of payment<br>increases.</p></div>
  <div class="item" style="left:755px;top:2226px"><div class="feature-title">VIVAMUS EFFICITUR</div><p class="feature-text">As more and more people own cryptocurrencies,<br>interest in using them as a means of payment<br>increases.</p></div>
</section>

<section class="partners abs">
  <div class="partner" style="left:179px"><i></i>Keelwave</div>
  <div class="partner" style="left:320px">Dunmore</div>
  <div class="partner" style="left:455px">Pallsto</div>
  <div class="partner" style="left:580px">Tidecrest</div>
  <div class="partner" style="left:732px">Marlowe</div>
  <div class="partner" style="left:873px">Quillo</div>
  <div class="partner" style="left:1014px">Stormvane</div>
</section>

<footer class="site-footer abs">
  <div class="footer-head" style="left:132px">LINKS</div>
  <span class="footer-link" style="left:132px;top:88px">Home</span>
  <span class="footer-link" style="left:132px;top:117px">Services</span>
  <span class="footer-link" style="left:132px;top:145px">Portfolio</span>
  <span class="footer-link" style="left:213px;top:88px">About</span>
  <span class="footer-link" style="left:213px;top:117px">Partners</span>
  <span class="footer-link" style="left:213px;top:145px">Contact Us</span>
  <div class="footer-head" style="left:359px">GET IN TOUCH</div>
  <span class="footer-link" style="left:359px;top:88px">Phone : 555 014 2290</span>
  <span class="footer-link" style="left:359px;top:117px">Email : hello@vextrel.example</span>
  <div class="footer-head" style="left:579px">CONTACT US</div>
  <div class="field" style="left:581px;top:91px;width:207px;height:30px">Name</div>
  <div class="field" style="left:581px;top:132px;width:207px;height:30px">Email</div>
  <div class="field" style="left:796px;top:91px;width:205px;height:71px">Message</div>
  <div class="send">SEND</div>
  <div class="rule"></div>
  <div class="copyright">Copyright © 2018 &nbsp;Vextrel. &nbsp;All rights reserved.</div>
  <span class="social" style="left:978px"></span>
  <span class="social" style="left:1012px"></span>
  <span class="social" style="left:1052px"></span>
</footer>
</body>
</html>
```